Doctor Formulated Medical Cosmetics

Halvessa Rue is an E-commerce site for high end Medical Cosmetics designed to treat specific skin problems. The Halvessa Rue difference/advantage is that all creams and serums are:
Doctor Formulated, Freshly Handmade, Registered Pharmacy.
The Site also provides real doctor Dermatology Consultations, Library (with a list of - 1. Active Ingredients in the creams with description of their effects, 2. Skin Conditions with information on what causes the condition and typical treatment approaches and outcomes. 3. Resources from Dermatology Journals and literature on the conditions.)
Header Information: Halvessa Rue, languages EN, BG, Register / log in, Shopping Bag. This field should be narrow.
Categories (horizontal): Home, Face, Body, Hair Care, Skin Conditions, Doctor Consultation, Library
The Landing Page should have only one well organized picture, which is intended to create the feeling of luxury, freedom and relaxation. It will be large and will fill the whole screen. All text should be on transparent or similar color fields. Please use the color of the text to create also the feeling of conservative luxury.
Written message / image overlay Halvessa Rue(logo), Skin Care, Doctor Formulated, Freshly Handmade, Registered Pharmacy.
Please study the Landing Page of this site as an example: www.marivelta.com
Under the Landing Page, there should be a slider with 4 of our products.
Underneath: Four Blog Articles (large pictures for maximum impact and luxury text underneath).
Underneath: Banner for Dermatologist Consultation, (button for Start Your Case Now).
Underneath: Two pictures in a line - Library (with books), and Active Ingredients.
Footer: Philosophy, Categories, Customer Care
Please adhere to the color palate provided in the pictures (as attachments). Provided are some examples of Web Sites with the desired look and feel. www.quillon.com , www.tavishrowe.com .
Please use different shades of gray, white, beige and gold colors, and black. Our products will be in brown glass jars and bottles to convey the professional, pharmacy made nature of the creams and lotions.
We find the following Front Page very attractive and effective - www.marivelta.com , with its full page image and overlaying text.
Please have a look at this link for the Landing page.
http://www.framstockly.com/detail/video/woman-lying-on-a-black-sand-beach-in-a-bikini-stock-footage/31862074
I would like to use it in the animated version to achieve the WOW effect. I have uploaded the jpeg version for it, so you will be able create your design.
For the Landing page design, please use only the two uploaded pictures of a woman laying at the beach. Let's see how each of them will look like.
Thank you for your help.

```html
<!DOCTYPE html>
<html lang="en">
<head>
<meta charset="utf-8">
<title>Halvessa Rue – Doctor Formulated Medical Cosmetics</title>
<link href="https://fonts.googleapis.com/css2?family=Cinzel:wght@400&family=Marcellus&family=Lato:ital,wght@0,400;0,700;1,400&display=swap" rel="stylesheet">
<style>
:root{
  --gold:#d3b36b;
  --gold-text:#c9a55e;
  --gold-deep:#b8954c;
  --ink:#222;
  --ink-soft:#444;
  --line:#d9d9d9;
  --white:#fff;
  --night:#121212;
  --footer:#1d1d1d;
  --footer-line:#555;
}
*{margin:0;padding:0;box-sizing:border-box}
html,body{width:1200px;height:2462px;overflow:hidden}
body{position:relative;background:var(--white);font-family:"Lato",sans-serif;color:var(--ink)}
.abs{position:absolute}

/* header */
.site-header{position:absolute;left:0;top:0;width:1200px;height:125px;background:var(--white)}
.utility-bar{position:absolute;left:476px;top:0;width:690px;height:39px;background:#262626;border-radius:0 0 24px 24px;display:flex;justify-content:space-around;align-items:center;padding:0 28px;color:#eee;font-size:13px}
.utility-bar span{display:flex;align-items:center;gap:6px}
.brand{position:absolute;left:58px;top:26px;display:flex;align-items:center;gap:14px}
.brand-mark{width:62px;height:62px;border:2px solid var(--gold);border-radius:50%}
.brand-name{font-family:"Marcellus",serif;font-size:42px;color:var(--gold);line-height:1}
.contact-item{position:absolute;top:58px;display:flex;align-items:center;gap:12px;font-size:15px;line-height:20px;color:var(--ink)}

/* nav */
.main-nav{position:absolute;left:0;top:125px;width:1200px;height:51px;background:var(--gold);border-top:1px solid #c6a45a;border-bottom:1px solid #c6a45a}
.main-nav ul{position:absolute;left:59px;top:0;display:grid;grid-template-columns:105px 95px 99px 144px 143px 246px 104px 144px;list-style:none;height:49px;border-left:1px solid #b99851}
.main-nav li{display:flex;align-items:center;justify-content:center;border-right:1px solid #b99851;font-size:14.5px;font-weight:700;color:#2a2210}

/* hero */
.hero{position:absolute;left:0;top:176px;width:1200px;height:440px;background:var(--night)}
.hero-photo{position:absolute;right:0;top:0;width:700px;height:440px;background:radial-gradient(ellipse at 62% 45%,#6b5a52 0%,#2e2624 45%,#121212 80%)}
.hero-title{position:absolute;left:58px;top:70px;font-family:"Cinzel",serif;font-size:42px;letter-spacing:1px;color:var(--gold)}
.advantages{position:absolute;left:58px;top:150px;list-style:none}
.advantages li{display:flex;align-items:center;gap:14px;height:54px;font-size:23px;color:var(--white)}
.slider-dots{position:absolute;left:570px;top:404px;display:flex;gap:10px;align-items:center}
.slider-dots i{width:14px;height:14px;border:2px solid #ddd;border-radius:50%}
.slider-dots i.active{width:20px;height:20px;background:var(--gold);border-color:var(--gold)}

/* section headings */
.section-title{position:absolute;left:0;width:1200px;text-align:center;font-family:"Marcellus",serif;font-size:35px;color:var(--ink)}
.section-title em{font-style:normal;color:var(--gold-text)}
.section-rule{position:absolute;left:59px;width:1080px;height:1px;background:var(--gold)}
.section-rule::after{content:"";position:absolute;left:530px;top:1px;border:10px solid transparent;border-top:7px solid #555;border-bottom:0}

/* products */
.products-bg{position:absolute;right:0;top:616px;width:200px;height:430px;background:linear-gradient(200deg,#e4e9d4 0%,#f3f5ec 50%,rgba(255,255,255,0) 100%)}
.product-card{position:absolute;top:727px;width:184px;height:279px;border:1px solid var(--line);background:var(--white);text-align:center}
.product-img{margin:18px auto 0;width:140px;height:150px;border-radius:4px}
.product-name{margin-top:22px;font-size:13.5px;line-height:20px;color:var(--ink)}
.product-price{margin-top:8px;display:flex;justify-content:center;align-items:center;gap:8px;font-weight:700;font-size:15px}
.cart-btn{width:34px;height:34px;border-radius:50%;background:var(--gold);display:flex;align-items:center;justify-content:center}
.slide-arrow{position:absolute;top:816px;width:37px;height:54px;display:flex;align-items:center;justify-content:center}

/* consultation */
.consult{position:absolute;left:0;top:1075px;width:1200px;height:460px;background:linear-gradient(90deg,#dfe4e8 0%,#c9d0d6 60%,#b8c1c8 100%)}
.consult-photo{position:absolute;left:0;top:0;width:525px;height:460px;background:linear-gradient(90deg,#c8c2bc 0%,#e3e3e2 55%,#cfd5da 100%)}
.consult-products{position:absolute;left:854px;top:222px;width:296px;height:238px;background:linear-gradient(180deg,#b7bcc0 0%,#e4e6e8 60%,#d0d4d8 100%);border-radius:4px}
.consult-title{position:absolute;left:519px;top:52px;font-size:31px;color:var(--ink)}
.consult-text{position:absolute;left:519px;top:102px;width:530px;font-size:15.5px;line-height:23.6px;color:#333}
.call-btn{position:absolute;left:520px;top:271px;width:212px;height:42px;background:var(--gold);border:2px solid #efe0bb;border-radius:6px;display:flex;align-items:center;gap:12px;padding-left:8px;color:var(--white);font-size:22px}

/* articles */
.article{position:absolute;width:495px;height:174px;border:1px solid var(--line);background:var(--white)}
.article-img{position:absolute;left:0;top:0;width:164px;height:172px}
.article-body{position:absolute;left:185px;top:18px;width:295px}
.article-title{font-size:16px;color:var(--gold-text)}
.article-meta{margin-top:12px;display:flex;align-items:center;gap:8px;font-size:13px;color:var(--ink)}
.article-meta span{display:flex;align-items:center;gap:5px;margin-right:8px}
.article-text{margin-top:10px;font-size:14px;line-height:19px;color:var(--ink)}
.read-more{position:absolute;right:0;bottom:0;width:107px;height:26px;background:var(--gold);color:var(--white);font-size:13.5px;display:flex;align-items:center;justify-content:center}

/* newsletter */
.newsletter{position:absolute;left:0;top:2104px;width:1200px;height:76px;background:var(--gold)}
.news-icon{position:absolute;left:95px;top:10px;width:56px;height:56px;border-radius:50%;background:var(--white);border:2px solid #333;display:flex;align-items:center;justify-content:center}
.news-title{position:absolute;left:177px;top:10px;font-size:24px;color:var(--white)}
.news-sub{position:absolute;left:177px;top:42px;font-size:15px;font-style:italic;color:var(--white)}
.news-input{position:absolute;left:542px;top:20px;width:427px;height:43px;border:1px solid #f2e6c8;background:var(--gold);color:var(--white);font-size:12px;font-style:italic;padding-left:14px;display:flex;align-items:center}
.news-btn{position:absolute;left:990px;top:20px;width:118px;height:43px;background:var(--white);font-size:13px;font-weight:700;display:flex;align-items:center;justify-content:center;letter-spacing:.5px}

/* footer */
.site-footer{position:absolute;left:0;top:2180px;width:1200px;height:282px;background:radial-gradient(ellipse at 50% 40%,#2c2c2c 0%,var(--footer) 70%);color:#e8e8e8}
.foot-heading{position:absolute;top:32px;font-size:18px;color:var(--white)}
.foot-rule{position:absolute;top:64px;height:1px;background:var(--footer-line)}
.philosophy{position:absolute;left:62px;top:78px;width:350px;font-size:13.5px;line-height:19px;text-align:justify}
.links{position:absolute;top:78px;list-style:none;font-size:14px;line-height:26px}
.links li::before{content:"›";color:var(--gold);margin-right:8px}
.contact-list{position:absolute;left:900px;top:76px;font-size:13px;line-height:18px}
.contact-list div{display:flex;gap:12px;margin-bottom:22px}
.copyright{position:absolute;left:59px;top:250px;font-size:12px}
.social{position:absolute;left:540px;top:243px;display:flex;gap:8px}
.social i{width:26px;height:26px;border-radius:50%;background:var(--gold)}
.accept{position:absolute;left:854px;top:250px;font-size:12px}
.cards{position:absolute;left:929px;top:244px;display:flex;gap:7px}
.cards i{width:36px;height:23px;background:var(--white);border-radius:2px}
</style>
</head>
<body>

<header class="site-header">
  <div class="utility-bar">
    <span><svg width="14" height="14" viewBox="0 0 14 14"><circle cx="7" cy="5" r="3" fill="none" stroke="#eee" stroke-width="1.5"/><path d="M2 13c1-3 3-4 5-4s4 1 5 4" fill="none" stroke="#eee" stroke-width="1.5"/></svg>Doctor</span>
    <span><svg width="16" height="14" viewBox="0 0 16 14"><rect x="2" y="5" width="12" height="8" fill="#eee"/><rect x="6" y="1" width="4" height="4" fill="none" stroke="#eee"/></svg>Pharmacy</span>
    <span><svg width="12" height="14" viewBox="0 0 12 14"><rect x="1" y="6" width="10" height="7" fill="#eee"/><path d="M3 6V4a3 3 0 0 1 6 0v2" fill="none" stroke="#eee" stroke-width="1.5"/></svg>Register / log in</span>
    <span><svg width="15" height="13" viewBox="0 0 15 13"><path d="M1 1h2l2 8h8l1-6H4" fill="none" stroke="#eee" stroke-width="1.5"/><circle cx="6" cy="11.5" r="1.3" fill="#eee"/><circle cx="12" cy="11.5" r="1.3" fill="#eee"/></svg>Shopping Cart</span>
    <span><svg width="20" height="13" viewBox="0 0 20 13"><rect width="20" height="13" fill="#2a3f8f"/><path d="M0 6.5h20M10 0v13" stroke="#fff" stroke-width="3"/><path d="M0 6.5h20M10 0v13" stroke="#c8202f" stroke-width="1.6"/></svg>English ▾</span>
  </div>

  <div class="brand">
    <span class="brand-mark"></span>
    <span class="brand-name">Halvessa Rue</span>
  </div>

  <div class="contact-item" style="left:763px">
    <svg width="34" height="40" viewBox="0 0 34 40"><path d="M8 4c3 0 4 6 3 8l-3 2c1 5 5 10 10 12l2-3c2-1 8 0 8 3l-2 6c-14 2-26-14-24-26z" fill="none" stroke="var(--gold)" stroke-width="2.5"/></svg>
    <div>Call Us:<br>+123-456-789</div>
  </div>
  <div class="contact-item" style="left:939px">
    <svg width="38" height="40" viewBox="0 0 38 40"><path d="M3 14l32-11-6 34-10-12z M19 25l16-22" fill="none" stroke="var(--gold)" stroke-width="2.5"/></svg>
    <div>Mail Us:<br>info@halvessarue.com</div>
  </div>
</header>

<nav class="main-nav">
  <ul>
    <li>Home</li><li>Face</li><li>Body</li><li>Hair Care</li><li>Skin Concerns</li><li>Dermatologist Consultation</li><li>Library</li><li>Contact Us</li>
  </ul>
</nav>

<section class="hero">
  <div class="hero-photo" role="img" aria-label="Portrait of a woman in black leather gloves against a dark background"></div>
  <h1 class="hero-title">Product Advantage</h1>
  <ul class="advantages">
    <li><svg width="28" height="22" viewBox="0 0 28 22"><path d="M2 11h20M15 4l8 7-8 7" fill="none" stroke="var(--gold)" stroke-width="2.5"/></svg>Doctor Formulated</li>
    <li><svg width="28" height="22" viewBox="0 0 28 22"><path d="M2 11h20M15 4l8 7-8 7" fill="none" stroke="var(--gold)" stroke-width="2.5"/></svg>Freshly Handmade</li>
    <li><svg width="28" height="22" viewBox="0 0 28 22"><path d="M2 11h20M15 4l8 7-8 7" fill="none" stroke="var(--gold)" stroke-width="2.5"/></svg>Registered Pharmacy</li>
    <li><svg width="28" height="22" viewBox="0 0 28 22"><path d="M2 11h20M15 4l8 7-8 7" fill="none" stroke="var(--gold)" stroke-width="2.5"/></svg>Highest Ethical Standards</li>
  </ul>
  <div class="slider-dots"><i></i><i class="active"></i><i></i></div>
</section>

<section class="products">
  <div class="products-bg" role="img" aria-label="Olives and a jar of cream as soft background decoration"></div>
  <h2 class="section-title" style="top:642px">Our <em>Products</em></h2>
  <div class="section-rule" style="top:694px"></div>

  <div class="slide-arrow" style="left:61px;background:#e6e6e6"><svg width="16" height="16" viewBox="0 0 16 16"><path d="M14 8H3M8 3L3 8l5 5" fill="none" stroke="#fff" stroke-width="2"/></svg></div>
  <div class="slide-arrow" style="left:1101px;background:#2a2a2a"><svg width="16" height="16" viewBox="0 0 16 16"><path d="M2 8h11M8 3l5 5-5 5" fill="none" stroke="#fff" stroke-width="2"/></svg></div>

  <article class="product-card" style="left:117px">
    <div class="product-img" role="img" aria-label="Gold cream jar" style="background:radial-gradient(circle at 50% 55%,#e8d48a,#f7f2df 70%,#fff)"></div>
    <p class="product-name">Lorem ipsum dolor<br>sit amet consectetuer</p>
    <div class="product-price">$375,00<span class="cart-btn"><svg width="18" height="16" viewBox="0 0 15 13"><path d="M1 1h2l2 8h8l1-6H4" fill="none" stroke="#fff" stroke-width="1.5"/><circle cx="6" cy="11.5" r="1.3" fill="#fff"/><circle cx="12" cy="11.5" r="1.3" fill="#fff"/></svg></span></div>
  </article>
  <article class="product-card" style="left:378px">
    <div class="product-img" role="img" aria-label="Grey cosmetic tube" style="background:linear-gradient(90deg,#fff 35%,#8a8c8e 42%,#5e6062 58%,#fff 65%)"></div>
    <p class="product-name">Lorem ipsum dolor<br>sit amet consectetuer</p>
    <div class="product-price">$145,00<span class="cart-btn"><svg width="18" height="16" viewBox="0 0 15 13"><path d="M1 1h2l2 8h8l1-6H4" fill="none" stroke="#fff" stroke-width="1.5"/><circle cx="6" cy="11.5" r="1.3" fill="#fff"/><circle cx="12" cy="11.5" r="1.3" fill="#fff"/></svg></span></div>
  </article>
  <article class="product-card" style="left:639px">
    <div class="product-img" role="img" aria-label="Gold serum bottle" style="background:linear-gradient(90deg,#fff 42%,#e0b32a 46%,#b8860b 54%,#fff 58%)"></div>
    <p class="product-name">Lorem ipsum dolor<br>sit amet consectetuer</p>
    <div class="product-price">$375,00<span class="cart-btn"><svg width="18" height="16" viewBox="0 0 15 13"><path d="M1 1h2l2 8h8l1-6H4" fill="none" stroke="#fff" stroke-width="1.5"/><circle cx="6" cy="11.5" r="1.3" fill="#fff"/><circle cx="12" cy="11.5" r="1.3" fill="#fff"/></svg></span></div>
  </article>
  <article class="product-card" style="left:900px">
    <div class="product-img" role="img" aria-label="Blue dropper bottle" style="background:linear-gradient(90deg,#fff 38%,#2f5fb8 44%,#1a3a80 56%,#fff 62%)"></div>
    <p class="product-name">Lorem ipsum dolor<br>sit amet consectetuer</p>
    <div class="product-price">$375,00<span class="cart-btn"><svg width="18" height="16" viewBox="0 0 15 13"><path d="M1 1h2l2 8h8l1-6H4" fill="none" stroke="#fff" stroke-width="1.5"/><circle cx="6" cy="11.5" r="1.3" fill="#fff"/><circle cx="12" cy="11.5" r="1.3" fill="#fff"/></svg></span></div>
  </article>
</section>

<section class="consult">
  <div class="consult-photo" role="img" aria-label="Dermatologist in a white coat talking with a patient"></div>
  <div class="consult-products" role="img" aria-label="Set of silver cosmetic bottles and jars"></div>
  <h2 class="consult-title">Dermatologist Consultation</h2>
  <p class="consult-text">Lorem ipsum dolor sit amet, consectetuer adipiscing elit, sed diam nonummy nibh euismod tincidunt ut laoreet dolore magna aliquam erat volutpat. Ut wisi enim ad minim veniam, quis nostrud exerci tation ullamcorper suscipit lobortis nisl ut aliquip ex ea commodo consequat. Duis autem vel eum iriure dolor in hendrerit.Lorem ipsum dolor sit amet, consectetuer adipiscing elit, sed diam nonummy nibh euismod tincidunt ut laoreet.</p>
  <div class="call-btn"><svg width="26" height="28" viewBox="0 0 34 40"><path d="M8 4c3 0 4 6 3 8l-3 2c1 5 5 10 10 12l2-3c2-1 8 0 8 3l-2 6c-14 2-26-14-24-26z" fill="#fff"/></svg>Call Us Today</div>
</section>

<section class="articles">
  <h2 class="section-title" style="top:1567px">Recent <em>Articles</em></h2>
  <div class="section-rule" style="top:1620px"></div>

  <article class="article" style="left:59px;top:1660px">
    <div class="article-img" role="img" aria-label="Woman with red curly hair" style="background:linear-gradient(135deg,#c2531f,#e6a27a)"></div>
    <div class="article-body">
      <h3 class="article-title">Lorem ipsum dolor sit amet</h3>
      <div class="article-meta"><span>◷ Aug 31, 2016</span><span>♥ 227</span><span>💬 2285</span></div>
      <p class="article-text">Lorem ipsum dolor sit amet, sed diamummy nibh euismod tincidunt ut dolore. Lorem ipsum dolor ipsum dolor sit.</p>
    </div>
    <span class="read-more">Read More</span>
  </article>
  <article class="article" style="left:643px;top:1660px">
    <div class="article-img" role="img" aria-label="Woman relaxing at a spa with flowers" style="background:linear-gradient(135deg,#f1e8e2,#c79a80)"></div>
    <div class="article-body">
      <h3 class="article-title">Lorem ipsum dolor sit amet</h3>
      <div class="article-meta"><span>◷ Aug 31, 2016</span><span>♥ 227</span><span>💬 2285</span></div>
      <p class="article-text">Lorem ipsum dolor sit amet, sed diamummy nibh euismod tincidunt ut dolore. Lorem ipsum dolor ipsum dolor sit.</p>
    </div>
    <span class="read-more">Read More</span>
  </article>
  <article class="article" style="left:59px;top:1881px">
    <div class="article-img" role="img" aria-label="Smiling blonde woman" style="background:linear-gradient(135deg,#e9d49a,#f3ddd0)"></div>
    <div class="article-body">
      <h3 class="article-title">Lorem ipsum dolor sit amet</h3>
      <div class="article-meta"><span>◷ Aug 31, 2016</span><span>♥ 227</span><span>💬 2285</span></div>
      <p class="article-text">Lorem ipsum dolor sit amet, sed diamummy nibh euismod tincidunt ut dolore. Lorem ipsum dolor ipsum dolor sit.</p>
    </div>
    <span class="read-more">Read More</span>
  </article>
  <article class="article" style="left:643px;top:1881px">
    <div class="article-img" role="img" aria-label="Smiling dark-haired woman" style="background:linear-gradient(135deg,#3a2a22,#e2cbbd)"></div>
    <div class="article-body">
      <h3 class="article-title">Lorem ipsum dolor sit amet</h3>
      <div class="article-meta"><span>◷ Aug 31, 2016</span><span>♥ 227</span><span>💬 2285</span></div>
      <p class="article-text">Lorem ipsum dolor sit amet, sed diamummy nibh euismod tincidunt ut dolore. Lorem ipsum dolor ipsum dolor sit.</p>
    </div>
    <span class="read-more">Read More</span>
  </article>
</section>

<section class="newsletter">
  <div class="news-icon"><svg width="24" height="18" viewBox="0 0 24 18"><rect x="1" y="1" width="22" height="16" fill="none" stroke="var(--gold-deep)" stroke-width="2"/><path d="M1 1l11 9 11-9" fill="none" stroke="var(--gold-deep)" stroke-width="2"/></svg></div>
  <h2 class="news-title">Join Our Newsletter!</h2>
  <p class="news-sub">Be the first one to know about our new Offers</p>
  <div class="news-input">Enter Your Email Here</div>
  <div class="news-btn">SUBSCRIBE</div>
</section>

<footer class="site-footer">
  <h3 class="foot-heading" style="left:62px">Our Philosophy</h3>
  <div class="foot-rule" style="left:62px;width:350px"></div>
  <p class="philosophy">Lorem ipsum dolor sit amet, consectetuer adipisemy nibh euismod tincidunt utre magmi aliquam erat volutpat. Ut wisi enim ad minim veniam quis nostrutation ullaeipit lobortis nisl ut aliquip nibh euismod tincidunt utre magmi aliquam erat volutpat .ipsum dolor sit amet, consectetuer adipisemy nibh euismod tincidunt utreipsum dolor.</p>

  <h3 class="foot-heading" style="left:484px">Quick Links</h3>
  <div class="foot-rule" style="left:484px;width:346px"></div>
  <ul class="links" style="left:484px"><li>Home</li><li>Face</li><li>Body</li><li>Hair Care</li><li>Skin Concerns</li></ul>
  <ul class="links" style="left:627px"><li>Dermatologist Consultation</li><li>Library</li><li>Contact Us</li><li>Our Doctors</li><li>Customer Care</li></ul>

  <h3 class="foot-heading" style="left:900px">Contact Details</h3>
  <div class="foot-rule" style="left:900px;width:239px"></div>
  <div class="contact-list">
    <div><svg width="14" height="20" viewBox="0 0 14 20"><path d="M7 19C2 12 1 9 1 7a6 6 0 0 1 12 0c0 2-1 5-6 12z" fill="var(--gold)"/><circle cx="7" cy="7" r="2.2" fill="var(--footer)"/></svg><span><b>Halvessa Rue</b><br>123 PG Duis Aute Irur Dolore<br>Srephenderit Amit In Voluptate</span></div>
    <div><svg width="16" height="16" viewBox="0 0 34 40"><path d="M8 4c3 0 4 6 3 8l-3 2c1 5 5 10 10 12l2-3c2-1 8 0 8 3l-2 6c-14 2-26-14-24-26z" fill="var(--gold)"/></svg><span style="font-size:14px">+123-456-789</span></div>
    <div><svg width="16" height="12" viewBox="0 0 24 18"><rect x="1" y="1" width="22" height="16" fill="var(--gold)"/><path d="M1 1l11 9 11-9" fill="none" stroke="var(--footer)" stroke-width="2"/></svg><span>info@halvessarue.com</span></div>
  </div>

  <p class="copyright">Copyright © 2016 Halvessa Rue. All Rights Reserved.</p>
  <div class="social" aria-label="Social links"><i></i><i></i><i></i><i></i></div>
  <p class="accept">We Accept :</p>
  <div class="cards" aria-label="Accepted payment methods"><i></i><i></i><i></i><i></i><i></i></div>
</footer>

</body>
</html>
```